Postcard Design Project

Cleaning service for house, apartments and condominiums.
Suggested inclusions are:We know you have better things to do with your time. We offer thorough, detailed cleaning services. So simply relax and leave the house cleaning to us!
100% Work Guaranteed
Lakeview Home Cleaning 512-738-294 Call Today!
Affordable, Reliable, Residential Cleaning Services
Enjoy a clean home without lifting a finger
www.lakeviewhomecleaning.example
an explosive burst with “20% Off First Cleaning”
Benefits of Using our Service
We clean the places you don’t have time to clean
We use our professional equipment and supplies
We use cleaning products that are gentle on your home

Industry/Entity Type

Cleaning Service

```html
<!DOCTYPE html>
<html lang="en">
<head>
<meta charset="utf-8">
<title>Lakeview Home Cleaning – Postcard</title>
<link href="https://fonts.googleapis.com/css2?family=Source+Sans+3:wght@300;400;600;700&display=swap" rel="stylesheet">
<style>
  :root{
    --green:#43a047;
    --green-dark:#3a9440;
    --green-soft:#82b46f;
    --tick-green:#7cc35f;
    --sky:#6ea9dc;
    --sky-deep:#4f8fcf;
    --panel-blue:#63a4d6;
    --footer-blue:#3576c0;
    --footer-blue-dark:#1f62b0;
    --pale:#e9f1fa;
    --white:#ffffff;
  }
  *{margin:0;padding:0;box-sizing:border-box}
  html,body{width:831px;height:1200px;overflow:hidden;background:var(--white)}
  body{position:relative;font-family:"Source Sans 3",sans-serif;color:var(--white)}
  .postcard{position:absolute;left:91px;width:651px;height:440px;overflow:hidden;background:var(--white);box-shadow:0 4px 12px rgba(0,0,0,.25)}
  .postcard--front{top:106px}
  .postcard--back{top:633px}

  .header{position:absolute;left:0;top:0;width:100%;height:102px;background:var(--green)}
  .header__stripe{position:absolute;left:0;bottom:0;width:100%;height:22px;background:var(--green-dark)}
  .brand{position:absolute;font-weight:400;color:var(--white);line-height:1.05;letter-spacing:.5px}
  .postcard--front .brand{right:42px;top:32px;font-size:24px;text-align:right}

  .photo{position:absolute;left:0;top:104px;width:100%;height:304px;background:linear-gradient(135deg,#8fbfe8 0%,var(--sky) 45%,var(--sky-deep) 100%)}
  .photo__overlay{position:absolute;inset:0}
  .headline{position:absolute;left:48px;top:66px;font-size:32px;font-weight:600;line-height:1}
  .sub{position:absolute;left:48px;top:102px;font-size:13.5px;font-weight:400;line-height:18px}
  .tick-block{position:absolute;left:0;top:186px;width:37px;height:51px;background:var(--tick-green)}
  .tick{position:absolute;left:45px;top:190px}
  .benefits{position:absolute;left:96px;top:180px;font-size:10px;line-height:13px}
  .benefits h3{font-size:12px;font-weight:700;line-height:15px}

  .offer{position:absolute;right:24px;top:195px;text-align:right}
  .offer__title{font-size:17px;font-weight:600}
  .offer__name{font-size:14.5px;font-weight:300;margin-top:4px}
  .offer__phone{font-size:36px;font-weight:700;line-height:1;margin-top:2px;text-shadow:0 2px 4px rgba(0,0,0,.35)}
  .offer__cta{font-size:14.5px;font-weight:300;margin-top:2px}

  .footer{position:absolute;left:0;bottom:0;width:100%;height:24px;background:var(--footer-blue)}
  .footer__url{position:absolute;right:26px;top:4px;font-size:11.5px}

  /* back */
  .header--split{background:var(--green)}
  .header__left{position:absolute;left:0;top:0;width:325px;height:102px;background:var(--green-soft)}
  .postcard--back .brand{left:52px;top:30px;font-size:24px}
  .panel{position:absolute;left:0;top:108px;width:325px;height:310px;background:var(--panel-blue)}
  .panel__lead{position:absolute;left:30px;top:48px;font-size:12px;font-weight:400}
  .panel__offer{position:absolute;left:30px;top:64px;font-size:20px;font-weight:600}
  .panel__offer b{font-size:25px;font-weight:700}
  .panel__benefits{position:absolute;left:30px;top:99px;font-size:10px;line-height:13px}
  .panel__benefits h3{font-size:13px;font-weight:700;line-height:16px}
  .panel__phone{position:absolute;left:30px;top:187px;font-size:23px;font-weight:700;line-height:1}
  .panel__cta{position:absolute;left:30px;top:212px;font-size:14.5px;font-weight:300}
  .staff-photo{position:absolute;left:172px;top:155px;width:150px;height:155px;background:linear-gradient(180deg,#6aa8d8 0%,#5d9f6a 60%,#e3c34a 100%);border-radius:4px}
  .mail-area{position:absolute;left:325px;top:108px;width:326px;height:310px}
  .footer--back{background:var(--footer-blue)}
  .footer__left{position:absolute;left:0;top:0;width:325px;height:100%;background:var(--footer-blue-dark)}
</style>
</head>
<body>

<section class="postcard postcard--front">
  <div class="header"><div class="header__stripe"></div></div>
  <div class="brand">Lakeview<br>Home Cleaning</div>

  <div class="photo" role="img" aria-label="Photo of a hand wiping a soapy window with a squeegee">
    <svg class="photo__overlay" width="651" height="304" viewBox="0 0 651 304">
      <polygon points="470,0 651,0 651,304 355,304" fill="#c9d8e6" opacity=".75"/>
      <polygon points="470,0 476,0 361,304 355,304" fill="#ffffff" opacity=".6"/>
    </svg>
    <h1 class="headline">100% Work Guaranteed</h1>
    <p class="sub">Affordable, Reliable, Residential Cleaning Services<br>Enjoy a clean home without lifting a finger</p>
    <div class="tick-block"></div>
    <svg class="tick" width="42" height="42" viewBox="0 0 42 42" aria-hidden="true">
      <circle cx="21" cy="21" r="18" fill="none" stroke="var(--tick-green)" stroke-width="4"/>
      <circle cx="21" cy="21" r="13" fill="var(--tick-green)"/>
      <polyline points="14,21 19,26 28,16" fill="none" stroke="#fff" stroke-width="3.5" stroke-linecap="round" stroke-linejoin="round"/>
    </svg>
    <div class="benefits">
      <h3>Benefits of Using our Service</h3>
      <p>We clean the places you don’t have time to clean</p>
      <p>We use our professional equipment and supplies</p>
      <p>We use cleaning products that are gentle on your home</p>
    </div>
    <div class="offer">
      <p class="offer__title">“20% Off First Cleaning”</p>
      <p class="offer__name">Lakeview Home Cleaning</p>
      <p class="offer__phone">512-738-294</p>
      <p class="offer__cta">Call Today!</p>
    </div>
  </div>

  <div class="footer"><span class="footer__url">www.lakeviewhomecleaning.example</span></div>
</section>

<section class="postcard postcard--back">
  <div class="header header--split"><div class="header__left"></div></div>
  <div class="brand">Lakeview<br>Home Cleaning</div>

  <div class="panel">
    <p class="panel__lead">An explosive burst with</p>
    <p class="panel__offer">“<b>20%</b> Off First Cleaning”</p>
    <div class="panel__benefits">
      <h3>Benefits of Using our Service</h3>
      <p>We clean the places you don’t have time to clean</p>
      <p>We use our professional equipment and supplies</p>
      <p>We use cleaning products that are gentle on your home</p>
    </div>
    <p class="panel__phone">512-738-294</p>
    <p class="panel__cta">Call Today!</p>
    <div class="staff-photo" role="img" aria-label="Photo of two smiling cleaners in aprons holding a broom, dustpan and spray bottle"></div>
  </div>

  <svg class="mail-area" width="326" height="310" viewBox="0 0 326 310" aria-hidden="true">
    <polygon points="0,0 160,0 30,310 0,310" fill="var(--pale)"/>
  </svg>

  <div class="footer footer--back">
    <div class="footer__left"></div>
    <span class="footer__url">www.lakeviewhomecleaning.example</span>
  </div>
</section>

</body>
</html>
```